Grand Chart of Bold Reformers

Hi - I would like your help transforming my (terrible) drawing into a graphic that pops -using hex colors I'll give you - so that I can put it into stationary and on t-shirts or tote bags. My company, the Marrowgate Institute, trains social change leaders (from the sectors in the periodic table) on how to lead large-scale change. I have this vision - the "periodic table" but these are the sectors that my clients work in. If you are having trouble reading my writing, I apologize. Our hex colors are: #114769, #76984C, #80B5CF (Seagull), #8F2C63 and Rangoon Black #191919. You don't need to use all of them, but it'd be good to be consistent with our overall branding. If you can't read my writing, I will send correct spelling. The "Marrowgate" with the flowers on the bottom is for a separate design bid.

Target Market(s)

nonprofit, social entrepreneurs, philanthropy, leaders

Requirements
Must have
• clean, readable font. alignment to look like periodic table of elements. heart icon for love, cat face for cats.

```html
<!DOCTYPE html>
<html lang="en">
<head>
<meta charset="utf-8">
<title>Grand Chart of Bold Reformers</title>
<link rel="stylesheet" href="https://fonts.googleapis.com/css2?family=Lato:wght@700;900&family=Roboto+Condensed:wght@400&display=swap">
<style>
  :root {
    --navy: #114769;
    --green: #76984C;
    --seagull: #80B5CF;
    --plum: #8F2C63;
    --ink: #191919;
    --paper: #ffffff;
    --tile: 130px;
    --pitch: 160px;
  }
  * { margin: 0; padding: 0; box-sizing: border-box; }
  html, body { width: 1200px; height: 1200px; overflow: hidden; background: var(--paper); }
  .chart {
    position: relative;
    width: 1200px;
    height: 1200px;
    background: var(--paper);
    font-family: "Lato", sans-serif;
  }
  .element {
    position: absolute;
    left: calc(120px + var(--col) * var(--pitch));
    top: calc(50px + var(--row) * var(--pitch));
    width: var(--tile);
    height: var(--tile);
    color: #fff;
    display: flex;
    flex-direction: column;
    align-items: center;
    justify-content: flex-start;
    padding-top: 10px;
  }
  .element::before {
    content: "";
    position: absolute;
    inset: 0;
    background: var(--fill);
    transform: rotate(var(--tilt, 8deg));
    z-index: 0;
  }
  .element::after {
    content: "";
    position: absolute;
    inset: -2px;
    border: 1.5px solid var(--navy);
    transform: rotate(var(--frame-tilt, 0deg));
    z-index: 1;
  }
  .element > * { position: relative; z-index: 2; }
  .element.navy { --fill: var(--navy); }
  .element.green { --fill: var(--green); }
  .element.seagull { --fill: var(--seagull); }
  .element.plum { --fill: var(--plum); }
  .symbol {
    font-weight: 700;
    font-size: 38px;
    line-height: 1;
  }
  .glyph {
    width: 46px;
    height: 46px;
    margin-top: 6px;
    fill: #fff;
    stroke: #fff;
  }
  .glyph-fill {
    width: 46px;
    height: 46px;
    margin-top: 6px;
    border-radius: 8px;
    background: rgba(255,255,255,0.55);
  }
  .name {
    font-family: "Roboto Condensed", sans-serif;
    font-size: 14px;
    line-height: 18px;
    margin-top: 6px;
    white-space: nowrap;
    max-width: 126px;
    text-align: center;
  }
  .name.long { font-size: 12px; letter-spacing: -0.2px; }
  .credit {
    position: absolute;
    left: 120px;
    top: 856px;
    font-family: "Roboto Condensed", sans-serif;
    font-size: 12px;
    color: var(--navy);
  }
  .wordmark {
    position: absolute;
    left: 0;
    right: 0;
    top: 930px;
    text-align: center;
    font-weight: 900;
    font-size: 120px;
    line-height: 1;
    color: var(--navy);
    letter-spacing: -2px;
  }
  .ground {
    position: absolute;
    left: 0;
    bottom: 0;
    width: 1200px;
    height: 110px;
  }
</style>
</head>
<body>
<main class="chart">
  <svg width="0" height="0" style="position:absolute">
    <defs>
      <symbol id="i-peace" viewBox="0 0 48 48"><circle cx="24" cy="24" r="19" fill="none" stroke-width="5"/><path d="M24 5v38M24 24L10.5 37.5M24 24l13.5 13.5" fill="none" stroke-width="5"/></symbol>
      <symbol id="i-heart" viewBox="0 0 48 48"><path d="M24 42 6 24C0 17 4 6 13 6c5 0 8 3 11 7 3-4 6-7 11-7 9 0 13 11 7 18z" stroke="none"/></symbol>
      <symbol id="i-house" viewBox="0 0 48 48"><path d="M24 6 3 24h6v18h11V31h8v11h11V24h6z" stroke="none"/></symbol>
      <symbol id="i-book" viewBox="0 0 48 48"><path d="M4 10c8-2 15-1 19 3v29c-4-3-11-4-19-2zM44 10c-8-2-15-1-19 3v29c4-3 11-4 19-2z" stroke="none"/></symbol>
      <symbol id="i-cap" viewBox="0 0 48 48"><path d="M24 8 2 18l22 10 22-10z" stroke="none"/><path d="M11 23v9c6 6 20 6 26 0v-9l-13 6z" stroke="none"/><path d="M42 20v14" fill="none" stroke-width="2.5"/></symbol>
      <symbol id="i-scales" viewBox="0 0 48 48"><path d="M24 6v34M12 42h24M8 12h32" fill="none" stroke-width="3"/><path d="M8 12 2 26h12zM40 12l-6 14h12z" fill="none" stroke-width="2"/><path d="M1 26c1 5 12 5 14 0zM33 26c1 5 12 5 14 0z" stroke="none"/></symbol>
      <symbol id="i-shield" viewBox="0 0 48 48"><path d="M24 3 6 10v12c0 12 8 20 18 23 10-3 18-11 18-23V10z" stroke="none"/><circle cx="24" cy="24" r="10" fill="var(--plum)" stroke="none"/><path d="m19 24 4 4 7-8" fill="none" stroke-width="3"/></symbol>
      <symbol id="i-headphones" viewBox="0 0 48 48"><path d="M8 30v-6a16 16 0 0 1 32 0v6" fill="none" stroke-width="4"/><rect x="5" y="28" width="10" height="15" rx="3" stroke="none"/><rect x="33" y="28" width="10" height="15" rx="3" stroke="none"/></symbol>
      <symbol id="i-briefcase" viewBox="0 0 48 48"><path d="M17 12V7h14v5" fill="none" stroke-width="4"/><rect x="4" y="12" width="40" height="28" rx="3" stroke="none"/><rect x="20" y="22" width="8" height="6" fill="var(--navy)" stroke="none"/></symbol>
      <symbol id="i-cat" viewBox="0 0 48 48"><path d="M7 4l10 9c2-.6 4.5-1 7-1s5 .4 7 1l10-9v22c0 10-7.5 18-17 18S7 36 7 26z" stroke="none"/></symbol>
    </defs>
  </svg>

  <!-- Row 1 -->
  <div class="element navy" style="--col:0;--row:0;--tilt:12deg;--frame-tilt:-2deg"><span class="symbol">Av</span><svg class="glyph"><use href="#i-peace"/></svg><span class="name">Anti Violence</span></div>
  <div class="element plum" style="--col:5;--row:0;--tilt:10deg;--frame-tilt:-2deg"><span class="symbol">B</span><div class="glyph-fill" role="img" aria-label="Box of belongings icon"></div><span class="name">Belonging</span></div>

  <!-- Row 2 -->
  <div class="element green" style="--col:0;--row:1;--tilt:-8deg;--frame-tilt:2deg"><span class="symbol">Ec</span><div class="glyph-fill" role="img" aria-label="Two children icon"></div><span class="name">Early Childhood</span></div>
  <div class="element seagull" style="--col:1;--row:1;--tilt:8deg;--frame-tilt:-1deg"><span class="symbol">Cc</span><div class="glyph-fill" role="img" aria-label="Globe and thermometer icon"></div><span class="name">Climate Change</span></div>
  <div class="element plum" style="--col:2;--row:1;--tilt:-7deg;--frame-tilt:2deg"><span class="symbol">Ej</span><div class="glyph-fill" role="img" aria-label="Hand holding a seedling icon"></div><span class="name long">Enviromental Justice</span></div>
  <div class="element navy" style="--col:3;--row:1;--tilt:9deg;--frame-tilt:-1deg"><span class="symbol">Hs</span><div class="glyph-fill" role="img" aria-label="Hand supporting a person icon"></div><span class="name">Human Services</span></div>
  <div class="element green" style="--col:4;--row:1;--tilt:-9deg;--frame-tilt:1deg"><span class="symbol">Hl</span><div class="glyph-fill" role="img" aria-label="Hands with medical cross icon"></div><span class="name">Health L.</span></div>
  <div class="element seagull" style="--col:5;--row:1;--tilt:7deg;--frame-tilt:-2deg"><span class="symbol">H</span><svg class="glyph"><use href="#i-house"/></svg><span class="name">Housing</span></div>

  <!-- Row 3 -->
  <div class="element plum" style="--col:0;--row:2;--tilt:9deg;--frame-tilt:-1deg"><span class="symbol">Ed</span><svg class="glyph"><use href="#i-book"/></svg><span class="name">Educational</span></div>
  <div class="element navy" style="--col:1;--row:2;--tilt:-8deg;--frame-tilt:2deg"><span class="symbol">As</span><svg class="glyph"><use href="#i-cap"/></svg><span class="name">A. School</span></div>
  <div class="element green" style="--col:2;--row:2;--tilt:8deg;--frame-tilt:-2deg"><span class="symbol">Sj</span><svg class="glyph"><use href="#i-scales"/></svg><span class="name">Social Justice</span></div>
  <div class="element seagull" style="--col:3;--row:2;--tilt:-9deg;--frame-tilt:1deg"><span class="symbol">Cr</span><div class="glyph-fill" role="img" aria-label="Person holding a rights sign icon"></div><span class="name">Civil Rights</span></div>
  <div class="element plum" style="--col:4;--row:2;--tilt:7deg;--frame-tilt:-2deg"><span class="symbol">He</span><div class="glyph-fill" role="img" aria-label="Hands with medical cross icon"></div><span class="name">Health Equity</span></div>
  <div class="element navy" style="--col:5;--row:2;--tilt:-8deg;--frame-tilt:1deg"><span class="symbol">J</span><svg class="glyph"><use href="#i-briefcase"/></svg><span class="name">Jobs</span></div>

  <!-- Row 4 -->
  <div class="element seagull" style="--col:0;--row:3;--tilt:-9deg;--frame-tilt:2deg"><span class="symbol">Aw</span><div class="glyph-fill" role="img" aria-label="Hand holding a paw print icon"></div><span class="name">Animal Welfare</span></div>
  <div class="element green" style="--col:1;--row:3;--tilt:8deg;--frame-tilt:-1deg"><span class="symbol">C</span><svg class="glyph" role="img" aria-label="Cat head icon"><use href="#i-cat"/></svg><span class="name">Cats</span></div>
  <div class="element plum" style="--col:2;--row:3;--tilt:-7deg;--frame-tilt:2deg"><span class="symbol">Rj</span><svg class="glyph"><use href="#i-scales"/></svg><span class="name">Racial Justice</span></div>
  <div class="element navy" style="--col:3;--row:3;--tilt:9deg;--frame-tilt:-2deg"><span class="symbol">Ir</span><div class="glyph-fill" role="img" aria-label="Person holding a rights sign icon"></div><span class="name">I. Rights</span></div>
  <div class="element seagull" style="--col:4;--row:3;--tilt:-8deg;--frame-tilt:1deg"><span class="symbol">Bh</span><div class="glyph-fill" role="img" aria-label="Hands with medical cross icon"></div><span class="name long">Behavioral Health</span></div>
  <div class="element green" style="--col:5;--row:3;--tilt:9deg;--frame-tilt:-1deg"><span class="symbol">I</span><div class="glyph-fill" role="img" aria-label="Family of several generations icon"></div><span class="name long">Intergenerational</span></div>

  <!-- Row 5 -->
  <div class="element navy" style="--col:0;--row:4;--tilt:8deg;--frame-tilt:-2deg"><span class="symbol">L</span><svg class="glyph"><use href="#i-heart"/></svg><span class="name">Love</span></div>
  <div class="element plum" style="--col:1;--row:4;--tilt:-8deg;--frame-tilt:1deg"><span class="symbol">A</span><svg class="glyph"><use href="#i-shield"/></svg><span class="name">Authenticity</span></div>
  <div class="element seagull" style="--col:2;--row:4;--tilt:9deg;--frame-tilt:-1deg"><span class="symbol">H</span><svg class="glyph"><use href="#i-heart"/></svg><span class="name">Humility</span></div>
  <div class="element green" style="--col:3;--row:4;--tilt:-7deg;--frame-tilt:2deg"><span class="symbol">A</span><svg class="glyph"><use href="#i-headphones"/></svg><span class="name">Audacity</span></div>
  <div class="element navy" style="--col:4;--row:4;--tilt:8deg;--frame-tilt:-2deg"><span class="symbol">J</span><svg class="glyph"><use href="#i-scales"/></svg><span class="name">Justice</span></div>

  <p class="credit">Icons by Linnet from Glyphary.com</p>

  <div class="wordmark">marrowgate</div>

  <svg class="ground" viewBox="0 0 1200 110" preserveAspectRatio="none" aria-hidden="true">
    <path d="M150 110 Q600 -40 1050 110 Z" fill="var(--seagull)"/>
  </svg>
</main>
</body>
</html>
```